ARRIVAL OF MARTIN THE OLD COUSIN

Hello everyone !

Our establishment, on 57 in CAMBRAI will have the pleasure of welcoming MARTIN LE VIEUX COUSIN, idol of young people, on Friday May 13, 2022, from 7:00 p.m.
On the program, photo session and dedications.
A VIP table will be offered to share the meal with him!
Only 12 places available at his table!
The brasserie will offer a barbecue for the occasion.
Admission with meal: €15
Seating at the VIP table: €65 (starter - main course - dessert); Champagne.
Happy HOURS on beers and cocktails!
Reservation strongly recommended.

I remain at your disposal ;

To your ideas!

```html
<!DOCTYPE html>
<html lang="en">
<head>
<meta charset="utf-8">
<title>Arrival of Martin the Old Cousin</title>
<link href="https://fonts.googleapis.com/css2?family=Roboto:wght@300;400;700&family=Roboto+Condensed:wght@700;800;900&display=swap" rel="stylesheet">
<style>
  :root{
    --ink:#050308;
    --white:#ffffff;
    --yellow:#fff200;
    --orange:#ff6a00;
    --purple:#9b2bc6;
    --violet:#7a2a8a;
    --lilac:#a97bc9;
  }
  *{margin:0;padding:0;box-sizing:border-box}
  html,body{width:848px;height:1200px;overflow:hidden;background:var(--ink)}
  .poster{position:relative;width:848px;height:1200px;overflow:hidden;background:var(--ink);font-family:"Roboto",Arial,sans-serif;color:var(--white)}
  .shards{position:absolute;inset:0;width:848px;height:1200px}
  .portrait{position:absolute;left:20px;top:150px;width:500px;height:560px;
    background:radial-gradient(ellipse 38% 30% at 42% 30%, #c9604a 0%, #6a2a24 45%, transparent 75%),
               radial-gradient(ellipse 55% 40% at 50% 72%, #5b5a3a 0%, #2a2a2c 50%, transparent 80%);}
  .headline{position:absolute;left:361px;top:66px;line-height:1}
  .headline .thin{font-family:"Roboto",Arial,sans-serif;font-weight:300;color:var(--white)}
  .headline .heavy{font-family:"Roboto Condensed",Arial Narrow,sans-serif;font-weight:900;color:var(--yellow)}
  .headline .line{display:block;white-space:nowrap}
  .line-1{font-size:79px;letter-spacing:-1.5px}
  .line-2{font-size:80px;margin-top:-2px;letter-spacing:-1px}
  .line-3{font-size:80px;margin-top:-4px;letter-spacing:-1.5px}
  .program{position:absolute;left:556px;top:476px;font-size:25.5px;line-height:29.6px;color:var(--yellow)}
  .program h2{font-size:25.5px;font-weight:700;color:var(--white);line-height:29.6px}
  .seats{position:absolute;left:556px;top:714px;font-size:25.5px;line-height:29.6px;color:var(--yellow)}
  .seats .count{display:inline-block;width:35px;height:35px;border-radius:50%;background:var(--lilac);color:var(--white);font-weight:700;text-align:center;line-height:35px;vertical-align:middle;margin-top:-5px}
  .venue{position:absolute;left:0;top:716px;width:516px;height:81px;background:var(--white);display:flex;align-items:center;justify-content:center}
  .venue .name{font-family:"Roboto",Arial,sans-serif;font-weight:700;font-size:34px;color:var(--ink)}
  .date{position:absolute;left:360px;top:832px;font-family:"Roboto Condensed",Arial Narrow,sans-serif;font-weight:800;font-size:55px;line-height:49px;color:var(--orange)}
  .pricing{position:absolute;left:57px;top:1009px;font-size:25px;line-height:28.2px;color:var(--yellow)}
  .pricing b{font-weight:700}
  .booking{position:absolute;left:362px;top:1151px;width:486px;height:49px;background:var(--purple);color:var(--white);font-weight:700;font-size:23.5px;text-align:right;padding-right:1px;line-height:47px;white-space:nowrap}
</style>
</head>
<body>
<main class="poster">
  <div class="portrait" role="img" aria-label="Portrait photo of Martin the Old Cousin in a shiny dark jacket, arms crossed"></div>
  <svg class="shards" viewBox="0 0 1324 1873" preserveAspectRatio="none" aria-hidden="true">
    <polygon points="1040,0 1324,0 1324,330 450,1070" fill="var(--violet)" opacity="0.7"/>
    <polygon points="1324,340 1324,380 70,1115" fill="#5a5a55" opacity="0.55"/>
    <polygon points="1324,380 1230,420 70,1115" fill="#444" opacity="0.5"/>
    <polygon points="1230,420 1230,560 1085,680" fill="#6a1fa0" opacity="0.9"/>
    <polygon points="1020,565 1110,440 1155,530" fill="#b5a62a" opacity="0.85"/>
    <polygon points="680,790 780,760 815,890" fill="#555" opacity="0.6"/>
    <polygon points="150,20 198,40 162,120" fill="#3b1a5e"/>
    <polygon points="65,125 130,108 145,185" fill="#3a3a3a"/>
    <polygon points="960,1610 1060,1605 1095,1735" fill="#a99a2a" opacity="0.9"/>
    <polygon points="960,1610 1030,1605 1088,1680" fill="#3b1a5e" opacity="0.6"/>
  </svg>

  <h1 class="headline">
    <span class="line line-1 thin">ARRIVAL OF</span>
    <span class="line line-2"><span class="heavy">MARTIN</span><span class="thin"> THE</span></span>
    <span class="line line-3 heavy">OLD COUSIN</span>
  </h1>

  <section class="program">
    <h2>PROGRAM</h2>
    <p>Photo session<br>and Dedications.<br>A VIP table will be<br>offered to share<br>the meal with him!<br>Barbecue....</p>
  </section>

  <p class="seats">Only <span class="count">12</span> places<br>available<br>at his table</p>

  <div class="venue"><span class="name">Brasserie du Canal</span></div>

  <p class="date">Friday May 13, 2022<br>from 7:00 p.m.</p>

  <p class="pricing">Admission with Meal: <b>€15</b><br>Seating at the VIP table: <b>€65</b><br>(Starter - Main course - Dessert),Champagne.<br><b>Happy HOURS</b> on <b>Beers</b> and <b>Cocktails</b>!</p>

  <p class="booking">Reservation strongly recommended.</p>
</main>
</body>
</html>
```